Report Cover and Format For Company

Hello, I would like a report cover for my company and document format that will be used for reports, proposals and documents to customers.

Industry/Entity Type

Information Technology

```html
<!DOCTYPE html>
<html lang="en">
<head>
<meta charset="utf-8">
<title>Northbeam Systems – Report Cover and Letterhead</title>
<link rel="stylesheet" href="https://fonts.googleapis.com/css2?family=Open+Sans:wght@400;600;700&family=Questrial&display=swap">
<style>
  :root {
    --backdrop: #d8d9db;
    --cover-black: #101010;
    --paper: #f4f4f4;
    --brand-blue: #2d6aa5;
    --accent-cyan: #35b3d4;
    --ink: #1e1e1e;
    --ink-soft: #555;
    --faint: #dfe3ea;
    --signature: #e6e6e6;
  }
  * { box-sizing: border-box; margin: 0; padding: 0; }
  html, body { width: 1200px; height: 800px; overflow: hidden; }
  body { background: var(--backdrop); font-family: "Open Sans", Arial, sans-serif; position: relative; }

  .sheet { position: absolute; top: 83px; width: 458px; height: 645px; }
  .report-cover { left: 90px; background: var(--cover-black); }
  .letterhead { left: 668px; background: var(--paper); }

  .brand-name {
    font-family: "Questrial", Arial, sans-serif;
    color: var(--brand-blue);
    text-transform: uppercase;
    display: flex; align-items: center; gap: 8px;
    line-height: 1;
  }
  .brand-square { background: var(--brand-blue); flex: none; }

  .report-cover .brand-name {
    position: absolute; left: 0; right: 0; top: 350px;
    justify-content: center; font-size: 21px; letter-spacing: 1px;
  }
  .report-cover .brand-square { width: 22px; height: 22px; }
  .cover-web {
    position: absolute; left: 0; right: 0; bottom: 20px; text-align: center;
    font-family: "Questrial", Arial, sans-serif; font-size: 9px; letter-spacing: .3px;
    color: var(--brand-blue);
  }

  .letterhead .brand-name { position: absolute; left: 17px; top: 76px; font-size: 10px; gap: 5px; }
  .letterhead .brand-square { width: 10px; height: 10px; }

  .meta-bar { position: absolute; left: 0; top: 127px; width: 12px; height: 75px; background: var(--accent-cyan); }
  .meta { position: absolute; left: 14px; top: 128px; width: 53px; text-align: right; font-size: 6.5px; color: var(--ink-soft); line-height: 1.3; }
  .meta dt { font-weight: 700; color: var(--ink); }
  .meta dd { margin-bottom: 8px; }

  .letter { position: absolute; left: 85px; top: 128px; width: 333px; font-size: 8px; line-height: 1.22; color: var(--ink); }
  .recipient { margin-bottom: 10px; }
  .salutation { margin-bottom: 10px; }
  .letter-body p { text-align: justify; margin-bottom: 9px; }
  .closing { margin-top: 20px; }
  .closing p { margin-bottom: 10px; }
  .signature { width: 95px; height: 24px; background: var(--signature); margin-top: -4px; }

  .watermark-name {
    position: absolute; right: 14px; bottom: 30px;
    font-size: 22px; color: var(--faint);
  }
  .letterhead .watermark-name .brand-square { width: 22px; height: 22px; background: var(--faint); }

  .contact { position: absolute; left: 17px; top: 575px; font-size: 4.6px; color: var(--ink-soft); line-height: 1.55; }
  .contact-brand { font-family: "Questrial", Arial, sans-serif; font-size: 6px; color: var(--brand-blue); text-transform: uppercase; margin-bottom: 4px; }
  .contact-row { display: flex; align-items: flex-start; gap: 4px; }
  .contact-row svg { width: 5px; height: 5px; flex: none; margin-top: 1px; fill: var(--accent-cyan); }
</style>
</head>
<body>

<section class="sheet report-cover">
  <div class="brand-name"><span class="brand-square"></span>Northbeam Systems</div>
  <div class="cover-web">WWW.NORTHBEAMSYSTEMS.COM</div>
</section>

<section class="sheet letterhead">
  <div class="brand-name"><span class="brand-square"></span>Northbeam Systems</div>

  <div class="meta-bar"></div>
  <dl class="meta">
    <dt>To</dt><dd>Mauris Euismod</dd>
    <dt>Subject</dt><dd>Egestas Ornare</dd>
    <dt>Date</dt><dd>10,18,2016</dd>
  </dl>

  <article class="letter">
    <p class="recipient">To the General Director,<br>Calder Grove Incorporated.<br>20 / 07 /2014</p>
    <p class="salutation">Dear Sir / Madam</p>
    <div class="letter-body">
      <p>Lorem ipsum dolor sit amet, consectetuer adipiscing elit. Nam cursus. Morbi ut mi. Li balam enim leo, egestas id, condimentum at, laoreet mattis, massa. Sed eleifend nos ummy diam. Praesent mauris ante, elementum et, bibendum at, posuere sit amet, nib duis tincidunt lectus quis dui viverra vestibulum. Suspendisse vulputate aliquam dui. Nulla elementum dui ut augue. Aliquam vehicula mi at mauris. Maecenas placerat sea si at consequat rhoncus, sem nunc gravida justo.</p>
      <p>Sed laoreet aliquamlii amet, consectetuer adipiscing elit. Nam cursus. Morbi ut mi. Lie balam enim leo, egestas id, condimentum at, laoreet mattis, massa. Sed eleifend nos ummy diam. Praesent mauris ante, elementum et, bibendum at.</p>
      <p>Nulla elementum dui ut augue. consectetuer adipiscing elit. Nam cursus. Morbi ut ma balam enim leo, egestas id, condimentum at, laoreet mattis, massa. Sed eleifend nos ummy diam. Praesent mauris ante, elementum et, bibendum at, posuere sit amet, nib duis tincidunt lectus quis dui viverra vestibulum. Suspendisse vulputate aliquam duifi. Nulla elementum dui ut augue. Aliquam vehicula mi at mauris. Maecenas placerat sef si at consequat rhoncus, sem nunc gravida justo.Fusce suscipit varius mi. Cum sociisz tes, nascetur ridiculus mus. Nulla dui. Morbi nunc odio, gravida at, cursus nec, luctusi lorem.Maecenas tristique orci ac sem. amin deso as. Duis ultricies pharetra agna. Dai nec accumsan malesuada orci. Donec</p>
      <p>liquam vehicula mi at mauris. Maecenas placerat se si at consequat rhoncus, sem nim gravida justo.Fusce suscipit varius mi. Cum sociis tes, nascetur ridiculus mus. Nulla al Morbi nunc odio, gravida at, cursus nec, luctusi. lorem.Maecenas tristique orci ac seai amin deso as.</p>
    </div>
    <div class="closing">
      <p>Sincerely,</p>
      <p>Tobias Lindqvist.</p>
      <div class="signature" role="img" aria-label="Handwritten signature of the sender"></div>
    </div>
  </article>

  <div class="brand-name watermark-name"><span class="brand-square"></span>Northbeam</div>

  <address class="contact">
    <div class="contact-brand">Northbeam Systems</div>
    <div class="contact-row">
      <svg viewBox="0 0 10 10"><path d="M5 0a3.5 3.5 0 0 0-3.5 3.5C1.5 6 5 10 5 10s3.5-4 3.5-6.5A3.5 3.5 0 0 0 5 0zm0 5a1.4 1.4 0 1 1 0-2.8A1.4 1.4 0 0 1 5 5z"/></svg>
      <span>12 Larkfield Way<br>Ashbury, 04217</span>
    </div>
    <div class="contact-row">
      <svg viewBox="0 0 10 10"><path d="M2 0l2 2.5-1.2 1.3a6 6 0 0 0 3.4 3.4L7.5 6 10 8l-1.5 2C4 10 0 6 0 1.5z"/></svg>
      <span>555-014-2290</span>
    </div>
    <div class="contact-row">
      <svg viewBox="0 0 10 10"><circle cx="5" cy="5" r="4.2" fill="none" stroke="#35b3d4" stroke-width="1.2"/><path d="M1 5h8M5 1c-2 2.5-2 5.5 0 8M5 1c2 2.5 2 5.5 0 8" fill="none" stroke="#35b3d4" stroke-width=".8"/></svg>
      <span>www.northbeamsystems.com</span>
    </div>
    <div class="contact-row">
      <svg viewBox="0 0 10 10"><path d="M0 2h10v6H0z" fill="none" stroke="#35b3d4" stroke-width="1.2"/><path d="M0 2l5 3.5L10 2" fill="none" stroke="#35b3d4" stroke-width="1"/></svg>
      <span>info@northbeamsystems.com</span>
    </div>
  </address>
</section>

</body>
</html>
```